New (old) Business Card Design Project

I would like to purchase a customized version of a design you have previously submitted - https://www.artmarketly.example/design/7305126

I like the card above, and would like to use the same design, jus with my business name, HARLOWAY ASSET ADVISORS. I like the colors in the card above, as well as the font. The other side will have my name, company name, address, phone, email, website, plus disclosure text I will provide.

Target Market(s)

wealthy families

Industry/Entity Type

Financial Services

Contact Information for Business Card

logo on one side, on other my name, company, address, phone, email, website, disclosure language I will provide.

Colors

Designer to choose colors to be used in the design.

Requirements
Must have
• colors: Deep blue and white
Nice to have
• Please see the items I have uploaded, below.
Should not have
• Cheap, tacky look.

```html
<!DOCTYPE html>
<html lang="en">
<head>
<meta charset="UTF-8">
<title>Harloway Asset Advisors – Business Card</title>
<link rel="stylesheet" href="https://fonts.googleapis.com/css2?family=Cinzel:wght@400&family=Open+Sans:wght@400;700&family=Crimson+Text:ital@1&display=swap">
<style>
  :root {
    --navy: #1b2a55;
    --navy-deep: #172851;
    --navy-soft: #24366a;
    --ink: #1a1a1a;
    --link-blue: #3b4fa0;
    --white: #ffffff;
    --backdrop: #2b2b2b;
  }
  * { margin: 0; padding: 0; box-sizing: border-box; }
  html, body {
    width: 1200px; height: 900px; overflow: hidden;
    background: var(--backdrop);
  }
  .canvas {
    position: relative; width: 1200px; height: 900px;
    display: flex; flex-direction: column; align-items: center; justify-content: center;
    gap: 40px;
  }
  .card {
    position: relative; width: 700px; height: 400px;
  }
  .card--front { background: var(--white); }
  .card--back { background: var(--navy-deep); }

  .wordmark {
    position: absolute;
    font-family: "Cinzel", serif;
    font-weight: 400;
    letter-spacing: 3px;
    white-space: nowrap;
  }
  .card--front .wordmark {
    top: 110px; left: 180px; font-size: 30px; color: var(--navy);
  }

  .identity {
    position: absolute; top: 200px; right: 372px; text-align: right;
    font-family: "Open Sans", sans-serif;
  }
  .identity__name { font-weight: 700; font-size: 20px; color: var(--navy); letter-spacing: 0.3px; }
  .identity__title { font-size: 15px; color: var(--ink); letter-spacing: 0.3px; }

  .divider {
    position: absolute; top: 190px; left: 350px; width: 1px; height: 120px;
    background: var(--navy);
  }

  .contact {
    position: absolute; top: 196px; left: 378px;
    font-family: "Open Sans", sans-serif; font-size: 14px; line-height: 21px; color: var(--ink);
    list-style: none;
  }
  .contact__label { font-weight: 700; color: var(--navy); }
  .contact__web { color: var(--link-blue); }

  .card--back .wordmark {
    top: 130px; left: 0; width: 100%; text-align: center;
    font-size: 30px; color: var(--navy-soft);
  }
  .motto {
    position: absolute;
    font-family: "Crimson Text", serif; font-style: italic;
    font-size: 30px; color: var(--white);
  }
  .motto--grow { left: 150px; top: 300px; }
  .motto--protect { left: 330px; top: 250px; }
  .motto--endow { left: 520px; top: 200px; }
</style>
</head>
<body>
<main class="canvas">
  <section class="card card--front" aria-label="Card front">
    <div class="wordmark">HARLOWAY ASSET ADVISORS</div>
    <div class="identity">
      <p class="identity__name">EVERETT LANE</p>
      <p class="identity__title">MANAGING DIRECTOR</p>
    </div>
    <div class="divider"></div>
    <ul class="contact">
      <li><span class="contact__label">TEL:</span> 061-482 337 905</li>
      <li><span class="contact__label">EMAIL:</span> info@harloway.example</li>
      <li class="contact__web">www.harloway.example</li>
      <li>87, Linden Row</li>
      <li>Fairhaven, 30918</li>
    </ul>
  </section>

  <section class="card card--back" aria-label="Card back">
    <div class="wordmark">HARLOWAY ASSET ADVISORS</div>
    <p class="motto motto--grow">Grow</p>
    <p class="motto motto--protect">Protect</p>
    <p class="motto motto--endow">Endow</p>
  </section>
</main>
</body>
</html>
```